Loan broker seeks referral card design for real estate financing

We need a design for a referral card for people who recommend us for real estate financing. If the deal goes through, each referrer will receive €750.

Text similar to: Recommend me! For every successful real estate financing referral, you will receive €750. (Other suggestions are also welcome)

The size should be no larger than A5 format, or possibly even oblong.
The design should convey security and competence and include themes such as independent advice.

The design should also include the company logo and a photo of me. Naturally, the design should also include a link to my website: www.die-wandlinger.at, along with my phone number and email address: office@die-wandlinger.at

```html
<!DOCTYPE html>
<html lang="de">
<head>
<meta charset="utf-8">
<title>Empfehlungskarte – Wandlinger Finanzberatung</title>
<link href="https://fonts.googleapis.com/css2?family=Quicksand:wght@500;600;700&display=swap" rel="stylesheet">
<style>
  :root {
    --brand-blue: #2c5aab;
    --text-grey: #5a5a5a;
    --card-white: #fbfbfb;
    --page-bg: #e4e4e4;
    --photo-dark: #2a2022;
    --photo-warm: #7a5a55;
  }
  * { margin: 0; padding: 0; box-sizing: border-box; }
  html, body {
    width: 1200px; height: 1124px; overflow: hidden;
    background: var(--page-bg);
    font-family: "Quicksand", sans-serif;
  }
  .referral-card {
    position: absolute; left: 0; top: 139px;
    width: 1200px; height: 846px;
    background: var(--card-white);
    overflow: hidden;
  }
  .brand {
    position: absolute; left: 54px; top: 50px; height: 144px;
    display: flex; align-items: center;
  }
  .brand-mark {
    width: 141px; height: 141px; border-radius: 50%;
    border: 4px solid var(--brand-blue);
  }
  .brand-divider {
    width: 3px; height: 144px; background: var(--text-grey);
    margin: 0 10px 0 14px;
  }
  .brand-text { display: flex; flex-direction: column; gap: 4px; }
  .brand-name { color: var(--brand-blue); font-weight: 700; font-size: 26px; }
  .brand-tagline { color: var(--text-grey); font-weight: 600; font-size: 20px; }

  .offer-band {
    position: absolute; left: 0; top: 223px;
    width: 1200px; height: 452px;
    background: var(--brand-blue);
  }
  .offer-copy {
    position: absolute; left: 52px; top: 268px;
    color: #fff; font-weight: 700;
  }
  .offer-headline { font-size: 45px; line-height: 1; }
  .offer-text { font-size: 45px; line-height: 60px; margin-top: 40px; }
  .offer-amount { font-size: 76px; line-height: 1; margin-top: 6px; }

  .portrait-frame {
    position: absolute; left: 687px; top: 123px;
    width: 451px; height: 600px;
    border: 3px solid var(--brand-blue); border-radius: 22px;
    background: var(--card-white);
    padding: 5px;
  }
  .portrait {
    width: 100%; height: 100%; border-radius: 16px;
    background: linear-gradient(160deg, var(--photo-dark) 0%, var(--photo-warm) 45%, var(--photo-dark) 100%);
  }

  .contact-row {
    position: absolute; left: 39px; right: 39px; top: 762px;
    display: flex; justify-content: space-between; align-items: center;
    color: var(--text-grey); font-weight: 700; font-size: 30px;
  }
  .contact-item { display: flex; align-items: center; gap: 10px; white-space: nowrap; }
  .contact-icon {
    width: 39px; height: 39px; border-radius: 50%;
    background: var(--brand-blue);
    display: flex; align-items: center; justify-content: center;
    flex-shrink: 0;
  }
</style>
</head>
<body>
  <main class="referral-card">
    <header class="brand">
      <div class="brand-mark"></div>
      <div class="brand-divider"></div>
      <div class="brand-text">
        <span class="brand-name">Wandlinger Finanzberatung GmbH</span>
        <span class="brand-tagline">Finanzieren, Versichern, Vorsorgen</span>
      </div>
    </header>

    <section class="offer-band"></section>
    <section class="offer-copy">
      <h1 class="offer-headline">Empfehlen Sie mich weiter!</h1>
      <p class="offer-text">Für jede realisierte<br>Immobilienfinanzierung<br>erhalten Sie als Tippgeber</p>
      <p class="offer-amount">€ 750</p>
    </section>

    <figure class="portrait-frame">
      <div class="portrait" role="img" aria-label="Porträtfoto des Beraters im dunklen Sakko und weißen Hemd"></div>
    </figure>

    <footer class="contact-row">
      <div class="contact-item">
        <span class="contact-icon">
          <svg width="20" height="20" viewBox="0 0 24 24" fill="#fff"><path d="M6.6 10.8a15.1 15.1 0 0 0 6.6 6.6l2.2-2.2a1 1 0 0 1 1-.25 11.4 11.4 0 0 0 3.6.57 1 1 0 0 1 1 1V20a1 1 0 0 1-1 1A17 17 0 0 1 3 4a1 1 0 0 1 1-1h3.5a1 1 0 0 1 1 1c0 1.25.2 2.45.57 3.6a1 1 0 0 1-.25 1z"/></svg>
        </span>
        <span>(0316) 481 205</span>
      </div>
      <div class="contact-item">
        <span class="contact-icon">
          <svg width="20" height="16" viewBox="0 0 24 18" fill="none" stroke="#fff" stroke-width="2"><rect x="2" y="2" width="20" height="14" rx="1"/><path d="M2 3l10 7 10-7"/></svg>
        </span>
        <span>office@die-wandlinger.at</span>
      </div>
      <div class="contact-item">
        <span class="contact-icon">
          <svg width="22" height="22" viewBox="0 0 24 24" fill="none" stroke="#fff" stroke-width="1.8"><circle cx="12" cy="12" r="9"/><ellipse cx="12" cy="12" rx="4" ry="9"/><path d="M3 12h18M4.5 7.5h15M4.5 16.5h15"/></svg>
        </span>
        <span>www.die-wandlinger.at</span>
      </div>
    </footer>
  </main>
</body>
</html>
```